Website Design For Physical Therapy/Sports Massage Clinic

Hi! I am looking for a sleek, fun and functional new wordpress website for my physical therapy/sports massage clinic. My current site is www.quorvanmotion.com. As you can see it's very basic and well... boring. :) In addition to a fun new look, I would also love this to be mobile friendly.

In terms of add on services/widgets I would like to use Zindleby Booking + Veltro Consent so that people can schedule and fill out paperwork remotely. Both seem like easy add ons to any site, but just in case here are the sites for both to ensure compatibility with the new design.

https://secure.zindlebybooking.com/
https://www.veltroconsent.com/

Thanks for reading and I'm excited to get started. I would love to see designs that are modern, athlete minded and fun as those are my clients. Attached you will find two logos (one white and one blue).

Target Market(s)

Athletes and weekend warriors

Industry/Entity Type

Physical Therapy

Number of Pages Required

1 page

Font styles to use
Sans Serif

Requirements
Must have
• 1) A fun home page that is modern and easy to navigate and 2) a website that is compatible with Zindleby booking + veltro consent so that my patients can schedule and fill out their paperwork without me.

```html
<!DOCTYPE html>
<html lang="en">
<head>
<meta charset="utf-8">
<title>Quorvan Motion — Physical Health Therapy Center</title>
<link rel="stylesheet" href="https://fonts.googleapis.com/css2?family=Nunito+Sans:wght@300;400;600;700;800&display=swap">
<style>
:root{
  --orange:#f26522;
  --blue:#0d5aa7;
  --navy:#0b4c8c;
  --ink:#2b2b2b;
  --text:#555;
  --muted:#888;
  --line:#e4e4e4;
  --dark:#262626;
  --paper:#ffffff;
  --soft:#f3f3f3;
}
*{box-sizing:border-box;margin:0;padding:0}
html,body{width:1200px;height:3015px;overflow:hidden}
body{font-family:"Nunito Sans",Arial,sans-serif;color:var(--text);background:var(--paper);position:relative}
.abs{position:absolute}

/* header */
.site-header{position:absolute;left:0;top:0;width:1200px;height:100px;background:var(--paper)}
.brand{position:absolute;left:156px;top:24px;display:flex;align-items:center;gap:12px}
.brand-mark{width:40px;height:40px;background:var(--orange);border-radius:50%}
.brand-name{font-size:26px;font-weight:800;color:var(--blue);letter-spacing:.5px}
.schedule-call{position:absolute;right:158px;top:8px;text-align:right}
.schedule-call small{display:block;font-size:13px;color:#666}
.schedule-call strong{font-size:18px;font-weight:400;color:var(--blue)}
.main-nav{position:absolute;right:158px;top:68px;display:flex;gap:36px;font-size:11px;letter-spacing:.6px;color:#555}
.main-nav .current{color:var(--orange);border-bottom:1px solid var(--orange);padding-bottom:4px}

/* hero */
.hero{position:absolute;left:0;top:100px;width:1200px;height:402px;background:linear-gradient(180deg,#6a7889 0%,#9aa2a3 35%,#8a6c47 70%,#5b4428 100%)}
.hero-title{position:absolute;left:0;width:100%;top:138px;text-align:center;color:#fff;font-size:42px;font-weight:700;letter-spacing:2px}
.hero-sub{position:absolute;left:0;width:100%;top:188px;text-align:center;color:#fff;font-size:25px;font-weight:600}
.btn{display:inline-flex;align-items:center;justify-content:center;border-radius:20px;font-size:11px;font-weight:700;letter-spacing:.8px;text-transform:uppercase}
.btn-blue{background:var(--blue);color:#fff}
.hero .btn{position:absolute;left:533px;top:241px;width:134px;height:34px}
.slide-arrow{position:absolute;top:180px;width:44px;height:44px;border-radius:50%;display:flex;align-items:center;justify-content:center}
.slide-arrow.prev{left:-22px;background:rgba(255,255,255,.35)}
.slide-arrow.next{right:-22px;background:var(--orange)}

/* section heads */
.section-title{position:absolute;font-size:19px;font-weight:700;color:var(--ink)}
.section-kicker{position:absolute;font-size:13px;font-weight:700;color:var(--orange);text-transform:uppercase;display:flex;align-items:center;gap:12px}
.section-kicker::after{content:"";width:64px;height:2px;background:var(--orange)}

/* services */
.service-card{position:absolute;top:690px;width:280px;height:229px;border:1px solid var(--line);text-align:center;padding:50px 26px 0}
.service-icon{position:absolute;left:106px;top:-33px;width:68px;height:66px;background:#fff;border:1px solid var(--line);display:flex;align-items:center;justify-content:center}
.service-card h3{font-size:18px;font-weight:400;color:var(--ink);line-height:24px;margin-top:8px}
.service-card p{font-size:12px;line-height:16px;margin-top:10px;color:#666}
.read-more{position:absolute;left:0;width:100%;bottom:30px;font-size:10px;font-weight:700;color:#444;letter-spacing:.5px}
.read-more.active{color:var(--orange)}

/* booking band */
.booking-band{position:absolute;left:0;top:985px;width:1200px;height:438px;background:linear-gradient(90deg,#eef0ef 0%,#f6f6f4 50%,#efe9e4 100%)}
.booking-screen{position:absolute;left:130px;top:20px;width:510px;height:370px;border-radius:12px;background:linear-gradient(180deg,#3a3d42 0%,#e9eef0 14%,#f5f7f8 70%,#2e3034 100%)}
.booking-band h2{position:absolute;left:663px;top:120px;font-size:24px;font-weight:400;color:var(--ink);line-height:32px}
.booking-band p{position:absolute;left:663px;top:208px;width:390px;font-size:12px;line-height:17px;color:#666}
.booking-band .btn{position:absolute;left:663px;top:268px;width:173px;height:32px}

/* blog */
.blog-arrow{position:absolute;top:1484px;width:24px;height:24px;border-radius:50%;display:flex;align-items:center;justify-content:center}
.blog-post{position:absolute;top:1548px;width:280px}
.blog-photo{height:168px}
.blog-meta{display:flex;gap:14px;margin-top:14px}
.date-box{width:40px;height:40px;background:var(--navy);color:#fff;text-align:center;line-height:13px;padding-top:5px;flex:none}
.date-box b{display:block;font-size:16px}
.date-box span{font-size:10px}
.blog-post h4{font-size:14px;font-weight:400;color:var(--ink);line-height:17px;padding-top:3px}
.blog-post h4.active{color:var(--orange)}
.blog-post p{font-size:12px;line-height:15px;color:#666;margin-top:12px}

/* testimonials */
.testimonials{position:absolute;left:0;top:1879px;width:1200px;height:352px;background:#efefef}
.quote-arrow{position:absolute;top:180px;width:28px;height:28px;display:flex;align-items:center;justify-content:center}
.quote-arrow.prev{left:157px;border:1px solid #999;background:#fff}
.quote-arrow.next{left:1015px;background:var(--orange)}
.avatar{position:absolute;left:225px;top:131px;width:120px;height:120px;border-radius:50%;border:4px solid #fff;background:linear-gradient(160deg,#d9dadb,#9ea3a8)}
.quote-text{position:absolute;left:376px;top:145px;width:630px;font-size:13px;line-height:19px;color:#555}
.quote-name{position:absolute;left:376px;top:254px;font-size:20px;color:#444}
.quote-role{position:absolute;left:376px;top:284px;font-size:12px;color:#888}

/* cta */
.cta-band{position:absolute;left:0;top:2231px;width:1200px;height:181px;background:var(--navy);text-align:center;color:#fff}
.cta-band p{margin-top:38px;font-size:19px;line-height:23px}
.cta-band .btn{position:absolute;left:482px;top:117px;width:236px;height:34px;border:1px solid #fff;color:#fff}

/* footer */
.footer{position:absolute;left:0;top:2412px;width:1200px;height:543px;background:var(--dark);color:#ddd}
.footer h2{position:absolute;left:151px;top:54px;font-size:24px;font-weight:600;color:#fff}
.footer .section-kicker{left:151px;top:88px;text-transform:none;font-weight:400}
.footer-label{position:absolute;font-size:13px;letter-spacing:1px;color:#fff;text-transform:uppercase}
.footer-info{position:absolute;font-size:13px;line-height:19px;color:#ddd}
.field{position:absolute;left:151px;width:227px;height:27px;border:1px solid #bbb;border-radius:3px;font-size:10px;color:#ddd;padding:6px 8px}
.field.question{left:404px;width:227px;height:162px}
.submit{position:absolute;left:151px;top:446px;width:102px;height:32px;border:1px solid #fff;color:#fff}
.map{position:absolute;left:683px;top:0;width:517px;height:543px;background:linear-gradient(135deg,#e6e3dc 0%,#dedad2 50%,#e8e5de 100%)}

/* bottom bar */
.bottom-bar{position:absolute;left:0;top:2955px;width:1200px;height:60px;background:#f4f4f4;font-size:11px;color:#777}
.get-social{position:absolute;left:151px;top:22px;display:flex;align-items:center;gap:6px}
.get-social i{width:14px;height:14px;border-radius:50%;background:#aaa;display:inline-block}
.get-social i.first{background:var(--orange);margin-left:14px}
.copyright{position:absolute;right:158px;top:24px}
.to-top{position:absolute;left:1104px;top:-22px;width:34px;height:34px;border-radius:50%;background:var(--blue);display:flex;align-items:center;justify-content:center}
</style>
</head>
<body>

<header class="site-header">
  <div class="brand"><span class="brand-mark"></span><span class="brand-name">Quorvan Motion</span></div>
  <div class="schedule-call"><small>Please Call To Schedule</small><strong>(512) 555-0147</strong></div>
  <nav class="main-nav">
    <span class="current">HOME</span><span>ABOUT</span><span>SERVICES</span><span>NEW PATIENTS</span><span>PRICING</span><span>BLOG</span><span>CONTACT US</span>
  </nav>
</header>

<section class="hero" role="img" aria-label="Photo of a runner's legs and shoes on a grassy hilltop trail at dusk">
  <div class="slide-arrow prev"><svg width="10" height="12" viewBox="0 0 10 12"><path d="M7 1 2 6l5 5" stroke="#fff" stroke-width="2" fill="none"/></svg></div>
  <h1 class="hero-title">PAIN AND INJURY KEEPING</h1>
  <p class="hero-sub">You From Your Active Lifestyle?</p>
  <a class="btn btn-blue">View Services</a>
  <div class="slide-arrow next"><svg width="10" height="12" viewBox="0 0 10 12"><path d="M3 1l5 5-5 5" stroke="#fff" stroke-width="2" fill="none"/></svg></div>
</section>

<h2 class="section-title" style="left:157px;top:552px">Physical Health Therapy Center</h2>
<div class="section-kicker" style="left:157px;top:590px">Why Choose Us</div>

<article class="service-card" style="left:157px">
  <div class="service-icon"><svg width="34" height="30" viewBox="0 0 34 30"><circle cx="9" cy="6" r="4" fill="var(--orange)"/><rect x="2" y="14" width="30" height="5" fill="var(--orange)"/><rect x="4" y="19" width="3" height="9" fill="var(--orange)"/><rect x="27" y="19" width="3" height="9" fill="var(--orange)"/><path d="M16 13l8-9 4 2-7 7z" fill="var(--orange)"/></svg></div>
  <h3>Physical Therapy</h3>
  <p>Quorvan Motion offers comprehensive, results-driven rehabilitation and performance programs for active individuals of all ages.</p>
  <div class="read-more">READ MORE &nbsp;➜</div>
</article>
<article class="service-card" style="left:460px">
  <div class="service-icon"><svg width="30" height="32" viewBox="0 0 30 32"><circle cx="19" cy="4" r="4" fill="var(--orange)"/><path d="M8 12l8-3 5 6 6 1-1 3-7-1-3-3-2 6 5 4-2 7-3-1 1-5-6-4-4 6-3-2 5-8 1-6-3 2-2-2z" fill="var(--orange)"/></svg></div>
  <h3>Sport Specific Analysis and Training</h3>
  <p>Quorvan Motion offers video analysis and training for athletes looking to improve their run.</p>
  <div class="read-more active">READ MORE &nbsp;➜</div>
</article>
<article class="service-card" style="left:764px">
  <div class="service-icon"><svg width="34" height="30" viewBox="0 0 34 30"><circle cx="24" cy="5" r="4" fill="var(--orange)"/><rect x="2" y="15" width="30" height="5" fill="var(--orange)"/><rect x="4" y="20" width="3" height="8" fill="var(--orange)"/><rect x="27" y="20" width="3" height="8" fill="var(--orange)"/><path d="M6 14c2-5 8-7 12-4l-2 4z" fill="var(--orange)"/></svg></div>
  <h3>Wellness and Maintenance Care</h3>
  <p>Regular soft tissue work and functional evaluation helps support healing and continued recovery.</p>
  <div class="read-more">READ MORE &nbsp;➜</div>
</article>

<section class="booking-band">
  <div class="booking-screen" role="img" aria-label="Laptop showing the online booking calendar, on a softly lit clinic desk"></div>
  <h2>No need to Call or Visit our<br>Centre Personally!</h2>
  <p>Appointments are available in 30, 45, and 60 minute increments depending on your needs and available time.</p>
  <a class="btn btn-blue">Book Online Now</a>
</section>

<h2 class="section-title" style="left:157px;top:1463px">Latest Blog &amp; Article</h2>
<div class="section-kicker" style="left:157px;top:1502px">Suceess Stories</div>
<div class="blog-arrow" style="left:984px;border:1px solid #aaa"><svg width="8" height="10" viewBox="0 0 8 10"><path d="M6 1 2 5l4 4" stroke="#888" stroke-width="1.6" fill="none"/></svg></div>
<div class="blog-arrow" style="left:1019px;background:var(--orange)"><svg width="8" height="10" viewBox="0 0 8 10"><path d="M2 1l4 4-4 4" stroke="#fff" stroke-width="1.6" fill="none"/></svg></div>

<article class="blog-post" style="left:157px">
  <div class="blog-photo" role="img" aria-label="Physiotherapist treating a patient's neck" style="background:linear-gradient(135deg,#e9e4df,#c9b7a8)"></div>
  <div class="blog-meta"><div class="date-box"><b>03</b><span>May</span></div><h4>How Physiotherapists Help Related Injuries</h4></div>
  <p>Quisque nec tincidunt justo unc vestibulum posuere nequevel rhoncus arcu pharetra sed on pharetra nuntincidunt.</p>
</article>
<article class="blog-post" style="left:460px">
  <div class="blog-photo" role="img" aria-label="Therapist guiding a patient through a back stretch on a mat" style="background:linear-gradient(135deg,#d9e6ee,#8fb2c8)"></div>
  <div class="blog-meta"><div class="date-box"><b>25</b><span>May</span></div><h4 class="active">Physiotherapists Help Back and Neck Pain</h4></div>
  <p>Vivamus libero leomaximus ac eni ullamcorper interdum nisi am tellus risus consectetur in ullamcorper sodales.</p>
</article>
<article class="blog-post" style="left:764px">
  <div class="blog-photo" role="img" aria-label="Therapist explaining a spine model to a patient" style="background:linear-gradient(135deg,#e8e8e6,#b9b3a8)"></div>
  <div class="blog-meta"><div class="date-box"><b>30</b><span>May</span></div><h4>Hip and Knee Injuries and Joint Replacements</h4></div>
  <p>Vivamus libero leomaximus ac eni ullamcorper interdum nisi am tellus risus consectetur.</p>
</article>

<section class="testimonials">
  <h2 class="section-title" style="left:157px;top:54px">Testimonials</h2>
  <div class="section-kicker" style="left:157px;top:88px;text-transform:none;font-weight:600">What Clients Say</div>
  <div class="quote-arrow prev"><svg width="12" height="8" viewBox="0 0 12 8"><path d="M11 4H2M4 1 1 4l3 3" stroke="#333" stroke-width="1.4" fill="none"/></svg></div>
  <div class="avatar" role="img" aria-label="Portrait of the client giving the testimonial"></div>
  <p class="quote-text">You truly are one of the most generous and inspiring people I know. Your love and passion for helping people have a ripple effect far beyond anything you can imagine. You are a true testimony to always being a student, mentor, and trusted legend. Your belief in me and support will forever have a lasting impact. Thank you for all you do.</p>
  <div class="quote-name">Dalen Morrow</div>
  <div class="quote-role">CTO, Brindle Hall</div>
  <div class="quote-arrow next"><svg width="12" height="8" viewBox="0 0 12 8"><path d="M1 4h9M8 1l3 3-3 3" stroke="#fff" stroke-width="1.4" fill="none"/></svg></div>
</section>

<section class="cta-band">
  <p>No matter whether your condition was caused by a sport, work<br>accident or otherwise, we welcome the chance to serve you.</p>
  <a class="btn">Schedule an Appointment</a>
</section>

<footer class="footer">
  <h2>Contact Information</h2>
  <div class="section-kicker">Get in Touch with Us</div>
  <div class="footer-label" style="left:151px;top:130px">Location</div>
  <div class="footer-info" style="left:151px;top:156px">2180 Larkmoor Rd, #310<br>Dunhaven, TX 78000</div>
  <div class="footer-label" style="left:408px;top:138px">Contact</div>
  <div class="footer-info" style="left:408px;top:164px">+603-555-0192<br>info@quorvanmotion.com</div>
  <div class="footer-label" style="left:151px;top:237px">Send a Message</div>
  <div class="field" style="top:268px">Name</div>
  <div class="field" style="top:312px">Company Name</div>
  <div class="field" style="top:356px">Phone</div>
  <div class="field" style="top:400px">Email</div>
  <div class="field question" style="top:268px">Question</div>
  <a class="btn submit">Submit</a>
  <div class="map" role="img" aria-label="Street map with a pin marking the clinic on Larkmoor Rd"></div>
</footer>

<div class="bottom-bar">
  <div class="get-social">Get Social: <i class="first"></i><i></i><i></i><i></i></div>
  <div class="copyright">Copyright © 2016 &nbsp;Quorvan Motion. All Rights Reserved</div>
  <div class="to-top"><svg width="12" height="12" viewBox="0 0 12 12"><path d="M6 11V2M2 5l4-4 4 4" stroke="#fff" stroke-width="1.8" fill="none"/></svg></div>
</div>

</body>
</html>
```